Healthy living company needs logo / business card

We are looking for a business identity for our company that operates in the Health and Wellness area.
Our audience is those open to hearing about the links between ill health and chemicals in the home as well as how to boost their health naturally through nutrition. We show people how to eliminate those toxins and share the message with others.
We also work with and mentor people who want to build their own business, share the message and create a leveraged income.
Our business name is: Brivora
The tag line we have is: Simple Changes ยท Healthy Living
Output for the project is:
Logo and business card design (2 people on the card).
Our perspective is for a modern, natural, simple, clean design (web 2.0 feel) that will appeal to a broad age range and audience. It should feel professional but not formal. It should not seem medical.
The logo should not be a gradient nor overly complex. Colouring should only be one or two colours at most. They can be bright, we are tending to lean towards green for obvious reasons but open to your thoughts.
Simplicity is the key.
The business card needs to be two sided. We like having the logo and card details on the front and then reversed out on the back with the logo and name in white on the colour block.
Please see the attached card brief document about the card content.

```html
<!DOCTYPE html>
<html lang="en">
<head>
<meta charset="utf-8">
<title>Brivora – Identity and Business Card</title>
<link href="https://fonts.googleapis.com/css2?family=Source+Sans+3:wght@400;600&display=swap" rel="stylesheet">
<style>
  :root {
    --accent: #f9ae44;
    --ink: #222222;
    --paper: #ffffff;
  }
  * { margin: 0; padding: 0; box-sizing: border-box; }
  html, body {
    width: 1200px;
    height: 900px;
    overflow: hidden;
    background: var(--paper);
    font-family: "Source Sans 3", "Myriad Pro", sans-serif;
  }
  .canvas { position: relative; width: 1200px; height: 900px; }

  /* Primary lockup */
  .logo-lockup { position: absolute; left: 140px; top: 100px; width: 840px; height: 290px; }
  .logo-lockup .mark-dot { position: absolute; left: 20px; top: 20px; }
  .logo-lockup .brand-name {
    position: absolute; left: 328px; top: 62px;
    font-size: 140px; font-weight: 600; line-height: 1;
    color: var(--ink); letter-spacing: -2px;
  }
  .logo-lockup .tagline {
    position: absolute; left: 337px; top: 200px;
    font-size: 33px; font-weight: 400; color: var(--ink);
  }

  /* Business cards */
  .card {
    position: absolute; top: 470px; width: 488px; height: 258px;
    background: var(--paper); overflow: hidden;
    box-shadow: 0 6px 18px rgba(0,0,0,0.22);
  }
  .card-front { left: 124px; border-top-left-radius: 26px; }
  .card-back { left: 639px; border-top-right-radius: 46px; }

  .card-front .mark-dot { position: absolute; left: -50px; top: -30px; }
  .contact-list {
    position: absolute; right: 14px; top: 12px; text-align: right;
    color: var(--accent); font-size: 17px; line-height: 1;
  }
  .contact-list .person { margin-bottom: 11px; }
  .contact-list .person span { display: block; line-height: 15px; }
  .contact-list .line { display: block; margin-top: 10px; }
  .contact-list svg { vertical-align: -1px; margin-right: 3px; }
  .card-front .brand-name-large {
    position: absolute; left: 0; top: 140px;
    font-size: 140px; font-weight: 600; line-height: 1;
    color: var(--ink); letter-spacing: -2px;
  }

  .card-back .white-panel { position: absolute; left: 0; top: 0; width: 161px; height: 100%; background: var(--paper); }
  .card-back .mark-dot { position: absolute; left: 40px; top: 116px; }
  .card-back .brand-name-small {
    position: absolute; left: 12px; top: 208px;
    font-size: 31px; font-weight: 600; line-height: 1;
    color: var(--ink);
  }
  .card-back .tagline-small {
    position: absolute; left: 12px; top: 240px;
    font-size: 10px; color: var(--ink); white-space: nowrap;
  }
  .card-back .colour-block { position: absolute; left: 161px; top: 0; right: 0; bottom: 0; background: var(--accent); }
  .benefit-list {
    position: absolute; left: 175px; top: 24px; list-style: none;
    color: var(--paper); font-size: 22px; font-weight: 600;
    line-height: 21.6px; letter-spacing: -0.6px;
  }
</style>
</head>
<body>
<main class="canvas">

  <section class="logo-lockup" aria-label="Brivora logo">
    <svg class="mark-dot" width="260" height="260" viewBox="0 0 260 260" aria-hidden="true">
      <circle cx="130" cy="130" r="125" fill="var(--accent)"/>
    </svg>
    <div class="brand-name">Brivora</div>
    <div class="tagline">small steps . better days</div>
  </section>

  <section class="card card-front" aria-label="Business card front">
    <svg class="mark-dot" width="210" height="210" viewBox="0 0 210 210" aria-hidden="true">
      <circle cx="105" cy="105" r="100" fill="var(--accent)"/>
    </svg>
    <div class="contact-list">
      <div class="person"><span>name name name</span><span>01632 960 418</span></div>
      <div class="person"><span>name name name</span><span>01632 960 418</span></div>
      <span class="line">
        <svg width="14" height="10" viewBox="0 0 14 10" aria-hidden="true"><rect x="0.7" y="0.7" width="12.6" height="8.6" fill="none" stroke="currentColor" stroke-width="1.2"/><path d="M1 1 L7 6 L13 1" fill="none" stroke="currentColor" stroke-width="1.2"/></svg>hello@brivorahome.com
      </span>
      <span class="line">
        <svg width="16" height="12" viewBox="0 0 16 12" aria-hidden="true"><path d="M1 11 C3 5 8 2 15 2 L15 5 L12 5 C8 5 6 7 4 11 Z" fill="currentColor"/></svg>555 210 4477
      </span>
      <span class="line">http://www.brivorahome.com</span>
    </div>
    <div class="brand-name-large">Brivora</div>
  </section>

  <section class="card card-back" aria-label="Business card back">
    <div class="white-panel"></div>
    <svg class="mark-dot" width="80" height="80" viewBox="0 0 80 80" aria-hidden="true">
      <circle cx="40" cy="40" r="38" fill="var(--accent)"/>
    </svg>
    <div class="brand-name-small">Brivora</div>
    <div class="tagline-small">small steps . better days</div>
    <div class="colour-block"></div>
    <ul class="benefit-list">
      <li>Multiple Streams of Income</li>
      <li>Financial Freedom</li>
      <li>Own my Own Business</li>
      <li>More Time</li>
      <li>Personal Development</li>
      <li>Health and Vitality</li>
      <li>Help Others</li>
      <li>Meet New People</li>
      <li>Retirement Plan</li>
      <li>Leave a Legacy</li>
    </ul>
  </section>

</main>
</body>
</html>
```